Bref créative
Fun Blitz Web Site
Web site design
Games
www.funblitzevents.example
We offer games and activities for parties and events
left side
Please see attachment for full details
Site details
black logo
white logo

```html
<!DOCTYPE html>
<html lang="en">
<head>
<meta charset="utf-8">
<title>Fun Blitz Web Site</title>
<link rel="stylesheet" href="https://fonts.googleapis.com/css2?family=Arimo:ital,wght@0,400;0,700;1,700&display=swap">
<style>
:root{
  --bg-deep:#0d1a2b;
  --bg-mid:#1f3a58;
  --bg-glow:#3f6b93;
  --blue:#1d7fc4;
  --blue-light:#3aa3e6;
  --blue-dark:#0f4f86;
  --orange:#f39a1c;
  --orange-dark:#d8720a;
  --white:#ffffff;
  --ink:#333333;
  --ink-soft:#666666;
  --panel-dark:#1a1f26;
  --grey-line:#d6d6d6;
  --icon-tone:#4f7fb0;
}
*{box-sizing:border-box;margin:0;padding:0}
html,body{width:1200px;height:1096px;overflow:hidden}
body{
  font-family:"Arimo",Arial,sans-serif;
  background:radial-gradient(ellipse at 50% 35%,var(--bg-glow) 0%,var(--bg-mid) 40%,var(--bg-deep) 85%);
  position:relative;color:var(--ink);
}
.site-header{position:absolute;left:0;top:0;width:1200px;height:115px}
.brand{position:absolute;left:135px;top:22px;display:flex;align-items:center;gap:12px}
.brand-mark{width:44px;height:44px;background:var(--orange);border-radius:4px}
.brand-name{font-size:38px;font-weight:700;color:var(--white);letter-spacing:1px}
.main-nav{position:absolute;left:390px;top:50px;display:flex;gap:5px}
.main-nav a{display:block;padding:0 15px;height:44px;line-height:44px;font-size:15px;font-weight:700;color:var(--white);text-decoration:none;white-space:nowrap;
  background:linear-gradient(var(--orange),var(--orange-dark));border-radius:8px 8px 0 0}
.main-nav a.is-active{background:linear-gradient(var(--blue-light),var(--blue-dark))}
.live-help{position:absolute;left:930px;top:0;width:240px;height:105px;background:linear-gradient(var(--blue-light),var(--blue-dark));
  border-radius:0 0 12px 12px;color:var(--white);text-align:center;padding-top:10px}
.live-help .help-title{display:inline-block;background:var(--white);color:var(--blue-dark);font-weight:700;font-size:17px;padding:6px 18px;border-radius:16px}
.live-help .help-note{font-size:12px;margin-top:4px}
.live-help .help-phone{font-size:24px;font-weight:700;margin-top:6px}

.hero-video{position:absolute;left:135px;top:120px;width:690px;height:345px;background:var(--panel-dark);border:3px solid #0b1118;border-radius:6px;padding:10px}
.video-frame{position:absolute;left:12px;top:8px;width:510px;height:285px;background:linear-gradient(135deg,#5e7f3e,#9fb08a 45%,#3b4a5a);}
.video-controls{position:absolute;left:12px;top:296px;width:510px;height:36px;background:linear-gradient(#f2f2f2,#c9c9c9);display:flex;align-items:center;gap:10px;padding:0 10px;font-size:12px;color:var(--ink)}
.video-controls .track{flex:1;height:6px;background:#999;border-radius:3px}
.thumb-list{position:absolute;left:540px;top:8px;display:flex;flex-direction:column;gap:10px}
.thumb{width:120px;height:70px;border:2px solid #555}
.thumb:nth-child(1){background:linear-gradient(#6b8a8f,#3f5663)}
.thumb:nth-child(2){background:linear-gradient(#8fa3b5,#4b5c6c)}
.thumb:nth-child(3){background:linear-gradient(#2f5d8c,#1b2f4a)}
.thumb:nth-child(4){background:linear-gradient(#4b3a6a,#1c1b33)}

.activity-panel{position:absolute;left:825px;top:126px;width:345px;height:354px;background:linear-gradient(var(--blue-light),var(--blue));border-radius:0 8px 8px 0;padding:16px 18px;color:var(--white)}
.activity h3{font-size:17px;font-style:italic;font-weight:700}
.activity p{font-size:12px;font-style:italic;line-height:1.3;margin:4px 0 16px}

.event-cards{position:absolute;left:135px;top:485px;display:flex;gap:25px}
.event-card{width:240px;height:190px;background:var(--white);border-radius:4px;position:relative;box-shadow:0 4px 10px rgba(0,0,0,.4)}
.event-card h4{height:38px;line-height:38px;padding-left:10px;font-size:17px;font-weight:700;font-style:italic;color:var(--white);background:linear-gradient(var(--blue-light),var(--blue-dark));border-radius:4px 4px 0 0;white-space:nowrap}
.event-photo{margin:8px auto 0;width:220px;height:120px}
.event-card:nth-child(1) .event-photo{background:linear-gradient(#f2c9a0,#d88a6a)}
.event-card:nth-child(2) .event-photo{background:linear-gradient(#b7a79a,#6d5f57)}
.event-card:nth-child(3) .event-photo{background:linear-gradient(#a33a3a,#4a2a3a)}
.event-card:nth-child(4) .event-photo{background:linear-gradient(#c9d8e8,#6f8fab)}
.read-more{position:absolute;left:60px;bottom:-8px;background:linear-gradient(var(--orange),var(--orange-dark));color:var(--white);font-size:13px;font-weight:700;padding:6px 14px;border-radius:12px}

.info-band{position:absolute;left:135px;top:696px;width:1035px;height:309px;background:var(--white)}
.welcome{position:absolute;left:10px;top:10px;width:375px}
.welcome h2{font-size:26px;font-weight:700;color:var(--blue-dark)}
.welcome h2 span{color:var(--orange)}
.welcome p{font-size:11.5px;line-height:1.4;color:var(--ink-soft);margin-top:8px}
.quote-cta{position:absolute;left:0;top:200px;width:385px;height:100px}
.quote-person{position:absolute;left:10px;top:0;width:110px;height:100px;background:linear-gradient(#f3dcc7,#c99b7a)}
.quote-button{position:absolute;left:145px;top:12px;width:225px;height:78px;background:linear-gradient(var(--orange),var(--orange-dark));border-radius:10px;color:var(--white);text-align:center;padding-top:8px;white-space:nowrap}
.quote-button .small{font-size:18px;font-weight:700}
.quote-button .big{font-size:28px;font-weight:700;margin-top:2px}

.social-box{position:absolute;left:405px;top:10px;width:280px;height:290px;border:1px solid var(--grey-line)}
.social-box h5{height:28px;line-height:28px;padding-left:8px;background:var(--blue-dark);color:var(--white);font-size:13px}
.social-page{display:flex;gap:8px;padding:8px;align-items:center;font-size:12px}
.social-page .sq{width:44px;height:44px;background:var(--orange)}
.social-page .like{display:inline-block;border:1px solid #aaa;font-size:11px;padding:1px 6px;margin-top:4px}
.social-count{font-size:11px;padding:0 8px;color:var(--ink-soft)}
.friend-grid{display:grid;grid-template-columns:repeat(5,46px);gap:6px 8px;padding:8px}
.friend .pic{width:46px;height:46px;background:linear-gradient(#b9c6d3,#7b8a99)}
.friend span{display:block;font-size:9px;color:var(--ink-soft);text-align:center}
.social-foot{font-size:10px;padding:0 8px;color:var(--blue-dark)}

.contact-form{position:absolute;left:705px;top:10px;width:320px;height:290px;background:var(--panel-dark);border-radius:8px;padding:12px 16px;color:var(--white)}
.contact-form h5{font-size:22px;font-style:italic;font-weight:700;border-bottom:1px solid #444;padding-bottom:6px}
.field{display:flex;align-items:center;margin-top:10px;font-size:13px}
.field label{width:90px}
.field .input{flex:1;height:24px;background:var(--white);border-radius:2px}
.field.tall{align-items:flex-start}
.field.tall .input{height:78px}
.submit{position:absolute;right:16px;bottom:14px;background:linear-gradient(var(--blue-light),var(--blue-dark));font-size:14px;font-weight:700;padding:8px 16px;border-radius:4px}

.site-footer{position:absolute;left:135px;top:1030px;width:1035px;display:flex;justify-content:space-between;align-items:center;color:#c7d3df;font-size:12px}
.social-icons{display:flex;gap:6px}
.social-icons i{display:block;width:28px;height:28px;border-radius:4px;background:var(--icon-tone)}
</style>
</head>
<body>
<header class="site-header">
  <div class="brand"><div class="brand-mark"></div><div class="brand-name">Fun Blitz</div></div>
  <nav class="main-nav">
    <a class="is-active" href="#">Home</a><a href="#">About Us</a><a href="#">Signup</a><a href="#">Join Us</a><a href="#">Contact Us</a>
  </nav>
  <div class="live-help">
    <div class="help-title">LIVE HELP</div>
    <div class="help-note">click here to start chat</div>
    <div class="help-phone">800 555-0142</div>
  </div>
</header>

<section class="hero-video">
  <div class="video-frame" role="img" aria-label="Video still of a laser tag player in action"></div>
  <div class="video-controls">
    <svg width="14" height="14" viewBox="0 0 14 14"><path d="M2 1l11 6-11 6z" fill="#333"/></svg>
    <span>0:00 / 4:34</span><div class="track"></div><span>240p</span>
  </div>
  <div class="thumb-list">
    <div class="thumb" role="img" aria-label="Video thumbnail"></div>
    <div class="thumb" role="img" aria-label="Video thumbnail"></div>
    <div class="thumb" role="img" aria-label="Video thumbnail"></div>
    <div class="thumb" role="img" aria-label="Video thumbnail"></div>
  </div>
</section>

<aside class="activity-panel">
  <div class="activity"><h3>Laser Tag Parties</h3><p>We offer year round indoor or outdoor laser tag that is great for birthday parties</p></div>
  <div class="activity"><h3>Human Gyroscope Ride</h3><p>The gyroscope design allows for rides of unlimited length and thrill</p></div>
  <div class="activity"><h3>Giant Hamster Ball Races</h3><p>Giant hamster ball races are a great outdoor activity for any party</p></div>
  <div class="activity"><h3>3D Video Game Party</h3><p>No matter what your gaming level is we have fun for all</p></div>
</aside>

<section class="event-cards">
  <article class="event-card"><h4>Parties Events</h4><div class="event-photo" role="img" aria-label="Children at a party"></div><span class="read-more">Read More</span></article>
  <article class="event-card"><h4>Corporate Events</h4><div class="event-photo" role="img" aria-label="Corporate event guests"></div><span class="read-more">Read More</span></article>
  <article class="event-card"><h4>Non-Profit Events</h4><div class="event-photo" role="img" aria-label="Non-profit event crowd"></div><span class="read-more">Read More</span></article>
  <article class="event-card"><h4>Local Business Events</h4><div class="event-photo" role="img" aria-label="Local business event"></div><span class="read-more">Read More</span></article>
</section>

<section class="info-band">
  <div class="welcome">
    <h2>Welcome to <span>Fun Blitz</span></h2>
    <p>Turn any party into the event of a lifetime. Each Fun Blitz activity is designed for a party of between 8 to 60 guests and is more affordable than you might think. Parties start at only $149 and include a professional game instructor, free delivery, setup, tear down and cleanup.</p>
    <p>We offer a self contained 3D video game trailer, two person human gyroscope ride, giant hamster ball races and laser tag parties.</p>
  </div>
  <div class="quote-cta">
    <div class="quote-person" role="img" aria-label="Smiling customer service agent"></div>
    <div class="quote-button"><div class="small">Request an Event</div><div class="big">QUOTE NOW!</div></div>
  </div>

  <div class="social-box">
    <h5>Find us on Friendbook</h5>
    <div class="social-page"><div class="sq"></div><div>Fun Blitz on Friendbook<br><span class="like">Like</span></div></div>
    <div class="social-count">1,281 people like Fun Blitz</div>
    <div class="friend-grid">
      <div class="friend"><div class="pic"></div><span>Anna</span></div>
      <div class="friend"><div class="pic"></div><span>Ben</span></div>
      <div class="friend"><div class="pic"></div><span>Cara</span></div>
      <div class="friend"><div class="pic"></div><span>Dan</span></div>
      <div class="friend"><div class="pic"></div><span>Eve</span></div>
      <div class="friend"><div class="pic"></div><span>Finn</span></div>
      <div class="friend"><div class="pic"></div><span>Gina</span></div>
      <div class="friend"><div class="pic"></div><span>Hal</span></div>
      <div class="friend"><div class="pic"></div><span>Ivy</span></div>
      <div class="friend"><div class="pic"></div><span>Joe</span></div>
    </div>
    <div class="social-foot">Friendbook social plugin</div>
  </div>

  <form class="contact-form">
    <h5>Contact Us</h5>
    <div class="field"><label>Your Name:</label><div class="input"></div></div>
    <div class="field"><label>Your Email:</label><div class="input"></div></div>
    <div class="field"><label>Subject:</label><div class="input"></div></div>
    <div class="field tall"><label>Comments:</label><div class="input"></div></div>
    <div class="submit">SUBMIT QUERY</div>
  </form>
</section>

<footer class="site-footer">
  <span>Copyright © 2009, Fun Blitz. All Rights Reserved</span>
  <div class="social-icons">
    <i></i><i></i><i></i><i></i><i></i><i></i>
  </div>
</footer>
</body>
</html>
```